PLAIN PAGES wordpress site to capture emails

Refer to inspiration upload for list of sites that will be useful for you.

We need a site that will be used to capture emails from clients that follow us on social media. The site will be all text, pretty simple. I have a couple of text sites that I like and we can use them for an example.

Menu section will have home, archive, about.
Footer will have © and Website Privacy Policy | Legal and Policies
There will be some text on the home page and an email capture.

This site will be all text no pictures.

I discuss office politics so the text portions will have some questions and answers on this and then prompt for the visitor to subscribe to my email list.

The only purpose of the site is to build an email list from existing social media followers so the site will be pretty simple in and of itself.

• PLAIN PAGES, similar Q&A to uploaded pics.

I will use a template from letter pinecone dotcom for email capture.

I like the simple couriernew font family that is on both sites supplied in the uploads.
• If you use any color it needs to be very minimal.

```html
<!DOCTYPE html>
<html lang="en">
<head>
<meta charset="utf-8">
<title>Plain Pages — Scurrilous Office Politics</title>
<link href="https://fonts.googleapis.com/css2?family=Courier+Prime:wght@400;700&display=swap" rel="stylesheet">
<style>
  :root {
    --ink: #222222;
    --muted: #6d6d6d;
    --dark: #262626;
    --dark-line: #3a3a3a;
    --paper: #ffffff;
    --accent: #e8692a;
    --rule: #d4d4d4;
    --footer-bg: #ededed;
    --light: #f2f2f2;
  }
  * { box-sizing: border-box; margin: 0; padding: 0; }
  html, body { width: 764px; height: 1200px; overflow: hidden; }
  body {
    position: relative;
    background: var(--paper);
    color: var(--ink);
    font-family: "Courier Prime", "Courier New", monospace;
  }

  .masthead {
    position: absolute; left: 0; top: 0; width: 764px; height: 340px;
    background: var(--dark);
    color: var(--light);
  }
  .masthead-notch { position: absolute; left: 0; top: 338px; width: 764px; height: 30px; }
  .site-nav {
    position: absolute; left: 0; top: 0; width: 764px; height: 52px;
    border-bottom: 1px solid var(--dark-line);
    display: flex; align-items: center; justify-content: space-between;
    padding: 0 34px 0 30px;
  }
  .site-name { font-size: 16px; font-weight: 400; letter-spacing: 1px; color: var(--light); }
  .nav-links { display: flex; gap: 44px; list-style: none; font-size: 12px; letter-spacing: 1px; }
  .nav-links a { color: #bdbdbd; text-decoration: none; }
  .nav-links .current { color: var(--light); font-weight: 700; }

  .hero-title {
    position: absolute; left: 0; top: 96px; width: 764px; text-align: center;
    font-size: 25px; font-weight: 700; letter-spacing: 3px; line-height: 30px;
  }
  .hero-title .sub { font-weight: 400; letter-spacing: 4px; }

  .signup { position: absolute; left: 162px; top: 164px; display: flex; height: 34px; }
  .signup-field {
    width: 298px; background: var(--paper); color: var(--ink);
    font-size: 12px; font-weight: 700; letter-spacing: 1px;
    display: flex; align-items: center; padding-left: 14px;
  }
  .signup-button {
    width: 140px; background: var(--accent); color: var(--paper);
    font-size: 12px; font-weight: 700; letter-spacing: 1px;
    display: flex; align-items: center; justify-content: center;
  }
  .signup-note {
    position: absolute; left: 0; top: 222px; width: 764px; text-align: center;
    font-size: 11px; line-height: 15px; color: #8a8a8a;
  }

  .section-head { position: absolute; left: 0; top: 376px; width: 764px; text-align: center; }
  .kicker { font-size: 11px; letter-spacing: 1px; color: var(--muted); }
  .section-title { margin-top: 4px; font-size: 22px; font-weight: 700; letter-spacing: 2px; }
  .stripes { position: absolute; top: 410px; height: 10px; }
  .stripes.left { left: 30px; width: 204px; }
  .stripes.right { left: 530px; width: 204px; }

  .qa { position: absolute; left: 30px; width: 704px; font-size: 11px; line-height: 13px; }
  .qa-row { display: flex; }
  .qa-mark { width: 18px; font-size: 13px; font-weight: 700; flex: none; }
  .question { font-weight: 700; color: var(--ink); font-size: 11.5px; }
  .answer { margin-top: 8px; color: var(--muted); }
  .answer .qa-mark { color: var(--ink); }

  .site-footer {
    position: absolute; left: 0; top: 1153px; width: 764px; height: 47px;
    background: var(--footer-bg);
    display: flex; align-items: center; justify-content: center;
    font-size: 10px; color: #555555;
  }
</style>
</head>
<body>

<header class="masthead">
  <nav class="site-nav">
    <div class="site-name">PLAIN PAGES</div>
    <ul class="nav-links">
      <li><a class="current" href="#">HOME</a></li>
      <li><a href="#">ARCHIVE</a></li>
      <li><a href="#">ABOUT</a></li>
    </ul>
  </nav>
  <h1 class="hero-title">SCURRILOUS OFFICE POLITICS<br><span class="sub">STORIES.OTHERS.</span></h1>
  <form class="signup">
    <div class="signup-field">EMAIL ADDRESS</div>
    <div class="signup-button">SUBSCRIBE</div>
  </form>
  <p class="signup-note">Sign up for the legendary email newsletter<br>and get the news &amp; updates</p>
</header>
<svg class="masthead-notch" viewBox="0 0 764 30" aria-hidden="true">
  <path d="M0 0 H350 Q366 0 372 14 L382 28 L392 14 Q398 0 414 0 H764 V2 H0 Z" fill="var(--dark)"/>
</svg>

<section class="section-head">
  <p class="kicker">DAILY OFFICE POLITICS</p>
  <h2 class="section-title">QUESTIONS &amp; ANSWERS</h2>
</section>
<svg class="stripes left" viewBox="0 0 204 10" aria-hidden="true">
  <g stroke="var(--rule)" stroke-width="1"><line x1="0" y1="1.5" x2="204" y2="1.5"/><line x1="0" y1="4.5" x2="204" y2="4.5"/><line x1="0" y1="7.5" x2="204" y2="7.5"/></g>
</svg>
<svg class="stripes right" viewBox="0 0 204 10" aria-hidden="true">
  <g stroke="var(--rule)" stroke-width="1"><line x1="0" y1="1.5" x2="204" y2="1.5"/><line x1="0" y1="4.5" x2="204" y2="4.5"/><line x1="0" y1="7.5" x2="204" y2="7.5"/></g>
</svg>

<article class="qa" style="top:464px">
  <div class="qa-row question"><span class="qa-mark">Q.</span><span>Lorem Ipsum is simply dummy text of the printing and typesetting industr?</span></div>
  <div class="qa-row answer"><span class="qa-mark">A:</span><span>Lorem Ipsum is simply dummy text of the printing and typesetting industry. Lorem Ipsum has been the industry's standard dummy text ever since the 1500s, when an unknown printer took a galley of type and scrambled it to make a type specimen book. T</span></div>
</article>
<article class="qa" style="top:563px">
  <div class="qa-row question"><span class="qa-mark">Q.</span><span>Excepteur sint occaecat cupidatat non proident,?</span></div>
  <div class="qa-row answer"><span class="qa-mark">A:</span><span>Lorem Ipsum is simply dummy text of the printing and typesetting industry. Lorem Ipsum has been the industry's standard dummy text ever since the 1500s, when an unknown</span></div>
</article>
<article class="qa" style="top:642px">
  <div class="qa-row question"><span class="qa-mark">Q.</span><span>How much are subscriptions??</span></div>
  <div class="qa-row answer"><span class="qa-mark">A:</span><span>Lorem Ipsum is simply dummy text of the printing and typesetting industry. Lorem Ipsum has been the industry's standard dummy text ever since the 1500s, when an unknown</span></div>
</article>
<article class="qa" style="top:726px">
  <div class="qa-row question"><span class="qa-mark">Q.</span><span>Excepteur sint occaecat cupidatat non proident,?</span></div>
  <div class="qa-row answer"><span class="qa-mark">A:</span><span>Lorem Ipsum is simply dummy text of the printing and typesetting industry. Lorem Ipsum has been the industry's standard dummy text ever since the 1500s, when an unknown</span></div>
</article>
<article class="qa" style="top:816px">
  <div class="qa-row question"><span class="qa-mark">Q.</span><span>How much are subscriptions??</span></div>
  <div class="qa-row answer"><span class="qa-mark">A:</span><span>Lorem Ipsum is simply dummy text of the printing and typesetting industry. Lorem Ipsum has been the industry's standard dummy text ever since the 1500s, when an unknown</span></div>
</article>
<article class="qa" style="top:902px">
  <div class="qa-row question"><span class="qa-mark">Q.</span><span>Lorem Ipsum is simply dummy text of the printing and typesetting industr?</span></div>
  <div class="qa-row answer"><span class="qa-mark">A:</span><span>Lorem Ipsum is simply dummy text of the printing and typesetting industry. Lorem Ipsum has been the industry's standard dummy text ever since the 1500s, when an unknown printer took a galley of type and scrambled it to make a type specimen book. T</span></div>
</article>
<article class="qa" style="top:1004px">
  <div class="qa-row question"><span class="qa-mark">Q.</span><span>Lorem Ipsum is simply dummy text of the printing and typesetting industr?</span></div>
  <div class="qa-row answer"><span class="qa-mark">A:</span><span>Lorem Ipsum is simply dummy text of the printing and typesetting industry. Lorem Ipsum has been the industry's standard dummy text ever since the 1500s, when an unknown printer took a galley of type and scrambled it to make a type specimen book. T</span></div>
</article>

<footer class="site-footer">© Company name. Privacy Policy | Legal and Policies</footer>

</body>
</html>
```